Asian Pakistani: Wedding Invitation

Design a pakistani asian wedding invitation.
Islamic theme, with arabic text:

Text to be used:

Start with: bismillah and dua for marriage. (The Holy Quran chapter 25 verse 75 with arabic text and english translation below)

Mrs. Rubina Sohail wife of (late) Mr. Sohail Imran Qureshi
Cordially requests your company to grace the joyous occasion of the wedding of their beloved daughter
Mehreen Qureshi
Daughter of ( late) Mr Sohail Imran qureshi
with
Bilal Siddiqui
Son of Mr. Junaid Siddiqui & Mrs Shazia Siddiqui

Insha’Allah on Thursday 29th August 2019 at Velvet Orchard
12 Marlow Crescent, Croydon
CR7 2LP
Baraat Arrival 6:30

RSVP
Usman Qureshi 07700 900412
Tariq Mehmood 07700 900583
Faisal Butt 07700 900735

Target Market(s)

Muslims

Font styles to use
Script

Colors

Designer to choose colors to be used in the design.

Requirements
Must have
• stylish calligraphy Arabic lettering of the dua requested above
• Size:
• Long 4" x 9.5"
Nice to have
• ottoman empire: Art theme

```html
<!DOCTYPE html>
<html lang="en">
<head>
<meta charset="utf-8">
<title>Wedding Invitation – Mehreen &amp; Bilal</title>
<link href="https://fonts.googleapis.com/css2?family=Great+Vibes&family=Cormorant+Garamond:wght@400;500;600&display=swap" rel="stylesheet">
<style>
  :root {
    --page: #1a1a1a;
    --cream: #f5efe0;
    --cream-deep: #ece2c8;
    --gold: #c49a3c;
    --gold-light: #e2c477;
    --gold-dark: #9c7526;
    --ink: #4a3a26;
    --band: #ffffff;
  }
  * { box-sizing: border-box; margin: 0; padding: 0; }
  html, body { width: 849px; height: 1200px; overflow: hidden; }
  body {
    background: var(--page);
    font-family: "Cormorant Garamond", Georgia, serif;
    color: var(--ink);
    position: relative;
  }
  .card {
    position: absolute;
    left: 105px; top: 40px;
    width: 640px; height: 1120px;
    background: var(--cream);
    overflow: hidden;
  }
  .gold-art {
    position: absolute;
    background: linear-gradient(90deg, var(--gold-dark), var(--gold-light) 50%, var(--gold-dark));
    border-radius: 30px;
    opacity: .85;
  }
  .bismillah { left: 255px; top: 22px; width: 130px; height: 30px; }
  .verse-arabic { left: 60px; top: 80px; width: 520px; height: 56px; }
  .verse-english {
    position: absolute; left: 70px; top: 148px; width: 500px;
    text-align: center; font-size: 15px; line-height: 1.3; color: var(--ink);
  }
  .hosts {
    position: absolute; left: 50px; top: 210px; width: 540px;
    text-align: center; font-family: "Great Vibes", cursive;
    font-size: 27px; line-height: 1.2; color: var(--ink);
  }
  .hosts .name { color: var(--gold-dark); }
  .band {
    position: absolute; left: 0; top: 395px; width: 640px; height: 260px;
    background: var(--band);
    border-top: 3px solid var(--gold);
    border-bottom: 3px solid var(--gold);
  }
  .band::before, .band::after {
    content: ""; position: absolute; left: 20px; right: 20px; height: 1px; background: var(--gold);
  }
  .band::before { top: 8px; }
  .band::after { bottom: 8px; }
  .band-ornament { left: 220px; width: 200px; height: 22px; }
  .band-ornament.top { top: 375px; }
  .band-ornament.bottom { top: 663px; }
  .couple { position: absolute; left: 0; top: 410px; width: 640px; text-align: center; }
  .couple .bride, .couple .groom {
    font-family: "Great Vibes", cursive; font-size: 62px; line-height: 1;
    color: var(--gold);
  }
  .couple .parents { font-size: 16px; color: var(--ink); margin-top: 4px; }
  .couple .with {
    font-family: "Great Vibes", cursive; font-size: 40px; line-height: 1; color: var(--gold-dark);
    margin: 4px 0 2px;
  }
  .inshallah { left: 265px; top: 740px; width: 110px; height: 40px; }
  .details {
    position: absolute; left: 0; top: 800px; width: 640px;
    text-align: center; font-size: 21px; line-height: 1.3; color: var(--ink);
  }
  .rsvp {
    position: absolute; left: 48px; top: 975px;
    font-size: 15px; line-height: 1.35; color: var(--ink);
  }
  .rsvp h2 { font-size: 15px; font-weight: 600; }
</style>
</head>
<body>
  <main class="card">
    <div class="gold-art bismillah" role="img" aria-label="Bismillah in gold Arabic calligraphy"></div>
    <div class="gold-art verse-arabic" role="img" aria-label="Quran chapter 25 verse 75 in gold Arabic calligraphy"></div>
    <p class="verse-english">Those will be awarded the Chamber for what they patiently endured, and they will be received therein with greetings and [words of] peace. (Quran Ch. 25, Verse 75)</p>

    <p class="hosts"><span class="name">Mrs. Rubina Sohail</span> wife of (late) <span class="name">Mr. Sohail Imran Qureshi</span><br>Cordially requests your company to grace the joyous occasion<br>of the wedding of their beloved daughter</p>

    <div class="gold-art band-ornament top" role="img" aria-label="Gold scroll ornament"></div>
    <section class="band"></section>
    <div class="couple">
      <div class="bride">Mehreen Qureshi</div>
      <div class="parents">Daughter of ( late) Mr Sohail Imran qureshi</div>
      <div class="with">with</div>
      <div class="groom">Bilal Siddiqui</div>
      <div class="parents">Son of Mr. Junaid Siddiqui &amp; Mrs Shazia Siddiqui</div>
    </div>
    <div class="gold-art band-ornament bottom" role="img" aria-label="Gold scroll ornament"></div>

    <div class="gold-art inshallah" role="img" aria-label="Insha'Allah in gold Arabic calligraphy"></div>
    <p class="details">on Thursday 29th August 2019<br>at Velvet Orchard<br>12 Marlow Crescent, Croydon<br>CR7 2LP<br>Baraat Arrival: 6:30 pm</p>

    <section class="rsvp">
      <h2>RSVP</h2>
      <p>Usman Qureshi 07700 900412<br>Tariq Mehmood 07700 900583<br>Faisal Butt 07700 900735</p>
    </section>
  </main>
</body>
</html>
```